■概要 ・RWMへの出稿用バナー作成をしていただける方を募集します。 ---------------- ■注意点 ご提案頂きましたバナー案について、SNSへの投稿・Webサイトへのアップ等を行わないようにお願いします。 ※承諾頂ける方のみコンペへの参加をお願いします。 ---------------- ■依頼詳細 ・バナー内にテキストを挿入する場合は、テキストレイヤーで挿入してください。 ・テキストはおよそ1/4サイズで表示される事を考慮して制作して下さい。 ・配信時は制作したバナーがスマホの画面幅程度に縮小されて表示されます。テキストの可読性を考慮して制作お願いします ・バナー広告を見て、押したくなるようなバナー作成をお願いします。 ■ 参考サイト(配信サイト) https://advocate-mori.com/ ※対応方法の一部変更(9/27内容修正) ・コンペは今まで通り、1200×628 で行います。 ・採用になった作品の納品時に300×300のバナーを作成して頂き一緒に納品して頂きたいです ※300×300のバナーは採用バナーの簡易版としてつけて頂けると幸いです。 ⇒そのまま縮小というより、「メイン画像+社名(ロゴ)+一言キャッチ」くらい簡易的でOKです。 小さいバナーですので可読性を考慮して頂けると幸いです。 ■サイズと枚数 【コンペ】 ・1200 x 628 ・1枚 【納品時】 ・1200 x 628 → 1枚 ・300×300→ 1枚 ■納品ファイル ・フォトショップ形式(.psd) ■連絡事項 土日・祝日は対応することができません。 平日は9~18時までにご連絡いただければ、当日。 それ以降は翌日にご返信いたします。 ※RWMガイドラインに沿った内容である事 RWM掲載ガイドライン関連資料(https://help.zentrova.com/promopolicy/topic/4418203?hl=ja&ref_topic=5520671,7730412,) ※他で登録されているデザインや商標の転用など、他社の知的財産権を侵すこと ※他のクライアントへ既に提案した内容の転用など たくさんのウェブデザイナーの方からのご提案をお待ちしております。 |
クライアント様が気に入りましたので、採用致します。
これからも沢山募集しますので、よろしくお願い致します。

```html
<!DOCTYPE html>
<html lang="ja">
<head>
<meta charset="utf-8">
<title>弁護士 森 健一 バナー</title>
<link rel="stylesheet" href="https://fonts.googleapis.com/css2?family=Noto+Serif+JP:wght@500;700&family=Noto+Sans+JP:wght@400;500;700&family=Dancing+Script:wght@600&display=swap">
<style>
  :root {
    --teal: #45b3ac;
    --teal-dark: #2f9d96;
    --ink: #2b2b2b;
    --muted: #555;
    --white: #ffffff;
    --photo-light: #f3f5f7;
    --photo-mid: #b9c0c8;
    --photo-dark: #4a4f58;
  }
  * { margin: 0; padding: 0; box-sizing: border-box; }
  html, body { width: 1200px; height: 628px; overflow: hidden; background: var(--white); }
  .banner { position: relative; width: 1200px; height: 628px; overflow: hidden; background: var(--white); font-family: "Noto Sans JP", sans-serif; }

  .hero-photo {
    position: absolute; left: 0; top: 0; width: 1200px; height: 354px;
    background:
      radial-gradient(ellipse 380px 300px at 880px 330px, var(--photo-dark) 0%, rgba(74,79,88,0.55) 45%, rgba(74,79,88,0) 75%),
      linear-gradient(90deg, var(--white) 0%, var(--white) 30%, var(--photo-light) 50%, var(--photo-mid) 100%);
  }

  .lawyer-name { position: absolute; left: 60px; top: 64px; font-family: "Noto Serif JP", serif; color: var(--ink); }
  .lawyer-name .title { font-size: 34px; font-weight: 500; letter-spacing: 2px; }
  .lawyer-name .name { font-size: 50px; font-weight: 700; letter-spacing: 6px; margin-left: 10px; }
  .firm-name { position: absolute; left: 60px; top: 132px; display: flex; align-items: center; gap: 12px; font-family: "Noto Serif JP", serif; font-size: 20px; color: var(--muted); letter-spacing: 2px; }
  .firm-name::before, .firm-name::after { content: ""; width: 38px; height: 1px; background: var(--muted); }

  .career-badge { position: absolute; left: 914px; top: -6px; width: 280px; height: 280px; }
  .career-badge .label { position: absolute; left: 0; top: 42px; width: 280px; text-align: center; font-family: "Dancing Script", cursive; font-size: 44px; color: var(--white); }
  .career-badge .org { position: absolute; left: 30px; top: 118px; width: 220px; height: 40px; background: var(--white); color: var(--teal-dark); font-size: 20px; font-weight: 500; display: flex; align-items: center; justify-content: center; }
  .career-badge .year { position: absolute; left: 0; top: 172px; width: 280px; text-align: center; color: var(--white); font-size: 21px; line-height: 1.3; }

  .tagline-band { position: absolute; left: 0; top: 354px; width: 1200px; height: 52px; background: var(--teal); color: var(--white); font-size: 30px; font-weight: 700; letter-spacing: 2px; display: flex; align-items: center; justify-content: center; }

  .practice-list { position: absolute; left: 34px; top: 446px; width: 1150px; list-style: none; display: flex; flex-wrap: wrap; row-gap: 30px; color: var(--teal); }
  .practice-list li { display: flex; align-items: baseline; font-size: 42px; font-weight: 500; white-space: nowrap; }
  .practice-list .num { font-size: 26px; margin-right: 4px; }
  .practice-list li:nth-child(1) { width: 282px; }
  .practice-list li:nth-child(2) { width: 580px; }
  .practice-list li:nth-child(4) { width: 282px; }

  .cta-button { position: absolute; left: 880px; top: 536px; width: 290px; height: 60px; background: var(--teal); color: var(--white); font-size: 24px; display: flex; align-items: center; justify-content: center; gap: 10px; letter-spacing: 1px; }
</style>
</head>
<body>
<div class="banner">
  <div class="hero-photo" role="img" aria-label="紺のスーツに弁護士バッジを付けた男性の胸元の写真"></div>

  <h1 class="lawyer-name"><span class="title">弁護士</span><span class="name">森 健一</span></h1>
  <p class="firm-name">森川総合法律事務所</p>

  <div class="career-badge">
    <svg width="280" height="280" viewBox="0 0 280 280">
      <circle cx="140" cy="140" r="140" fill="var(--teal)" opacity="0.92"/>
      <circle cx="140" cy="140" r="128" fill="none" stroke="var(--white)" stroke-width="2"/>
    </svg>
    <div class="label">Career</div>
    <div class="org">浪速労働問題研究会</div>
    <div class="year">2012<br>弁護士登録</div>
  </div>

  <div class="tagline-band">個人の法律問題から専門的な事件まで</div>

  <ul class="practice-list">
    <li><span class="num">01</span>労働問題</li>
    <li><span class="num">02</span>インターネット問題</li>
    <li><span class="num">03</span>行政訴訟</li>
    <li><span class="num">04</span>環境問題</li>
    <li><span class="num">05</span>一般民事・家事事件</li>
  </ul>

  <a class="cta-button">
    <svg width="10" height="12" viewBox="0 0 10 12"><path d="M0 0 L10 6 L0 12 Z" fill="var(--white)"/></svg>
    詳しくはこちら
  </a>
</div>
</body>
</html>
```